Stationary Design For New Dynamic Company

Hi there we require stationary designed for our new company, we have used "Sketch Meadow" recently for our logo and were very impressed with all of the designers that contributed towards the final result.
What we require now is the following:
Letter head layout (A4)
Business Cards (5 people)
With Compliments slips
Envelopes
Email stationary
We would like to use our current logo design and I have included it for your use (JPEG is the one we have chosen and I have attached an EPS file for your use). Our company specializes in architectural cladding and our products are used by architects, builders and private clients, so we wish for the stationary to be suitable and attractive to our clientele.
I thank everyone in advance for your contributions.
Thank you to all that have provided your designs for this project, I apologize for not providing feedback as I have been away. I have looked at everyone's designs and they all look great and I will come back to those designers that I wish to have changes made sometime today.
Once again a big thank you to all involved.

```html
<!DOCTYPE html>
<html lang="en">
<head>
<meta charset="utf-8">
<title>Veranox Stationery</title>
<link href="https://fonts.googleapis.com/css2?family=Open+Sans:ital,wght@0,400;0,600;0,700;1,400&display=swap" rel="stylesheet">
<style>
:root{
  --navy:#1d2a7a;
  --orange:#f39200;
  --blue-dark:#1f4f8f;
  --blue-light:#4a7cb8;
  --paper:#ffffff;
  --backdrop:#e9e9e9;
  --edge:#d4d4d4;
}
*{margin:0;padding:0;box-sizing:border-box}
html,body{width:1200px;height:1200px;overflow:hidden}
body{background:var(--backdrop);font-family:"Open Sans",Arial,sans-serif;color:var(--navy);position:relative}
.sheet{position:absolute;background:var(--paper);border:1px solid var(--edge);overflow:hidden}
.plan-area{position:absolute;left:0;top:0}
.brand{position:absolute;font-weight:700;color:var(--navy);letter-spacing:.5px;white-space:nowrap}
.brand-mark{display:inline-block;background:var(--orange);vertical-align:middle;margin-right:.3em}

.showcase-brand{left:870px;top:62px;font-size:40px}
.showcase-brand .brand-mark{width:26px;height:26px}

.letterhead{left:72px;top:105px;width:698px;height:990px}
.letterhead .brand{left:165px;top:40px;font-size:24px}
.letterhead .brand-mark{width:16px;height:16px}
.letterhead .address{position:absolute;right:26px;top:37px;text-align:right;font-size:11.5px;line-height:16px}
.letterhead .tab{position:absolute;right:0;top:40px;width:8px;height:60px;background:var(--orange)}

.card-front{left:583px;top:290px;width:372px;height:188px}
.card-front .brand{left:100px;top:14px;font-size:17px}
.card-front .brand-mark{width:11px;height:11px}
.card-front .person{position:absolute;right:14px;top:68px;text-align:right;font-size:9.5px;line-height:13px}
.person .name{font-weight:700}
.person .role{color:var(--orange);font-style:italic}
.person .gap{height:11px}
.card-front .note{position:absolute;left:12px;bottom:8px;font-size:12px;font-style:italic;color:var(--orange)}

.card-back{left:672px;top:522px;width:355px;height:190px;background:var(--orange)}
.card-back .brand{right:14px;bottom:32px;font-size:18px;color:#fff}
.card-back .brand-mark{width:11px;height:11px;background:#fff}

.comp-slip{left:315px;top:690px;width:750px;height:450px}
.comp-slip .brand{left:255px;top:70px;font-size:30px}
.comp-slip .brand-mark{width:20px;height:20px}
.comp-slip .note{position:absolute;left:16px;top:290px;font-size:24px;font-style:italic;color:var(--orange)}
.comp-slip .footer{position:absolute;left:22px;right:22px;top:360px;display:flex;justify-content:space-between;font-size:10.5px}
.footer span{padding-left:10px;border-left:2px solid var(--orange)}
.footer span:first-child{border-left:none;padding-left:0}
</style>
</head>
<body>

<div class="brand showcase-brand"><span class="brand-mark"></span>VERANOX</div>

<section class="sheet letterhead">
  <svg class="plan-area" width="240" height="180" role="img" aria-label="Blue architectural floor plan drawing">
    <defs><linearGradient id="planLetter" x1="0" y1="0" x2="1" y2="1"><stop offset="0" stop-color="var(--blue-dark)"/><stop offset="1" stop-color="var(--blue-light)"/></linearGradient></defs>
    <polygon points="0,0 150,0 150,95 0,170" fill="url(#planLetter)"/>
  </svg>
  <div class="brand"><span class="brand-mark"></span>VERANOX</div>
  <div class="address">Veranox Partners Suite 4, The Yard<br>Kestrel Park, Ashford, AS12 3QR<br>T : 01632 960412<br>F : 01632 960587</div>
  <div class="tab"></div>
</section>

<section class="sheet card-front">
  <svg class="plan-area" width="100" height="100" role="img" aria-label="Blue architectural floor plan drawing">
    <defs><linearGradient id="planCard" x1="0" y1="0" x2="1" y2="1"><stop offset="0" stop-color="var(--blue-dark)"/><stop offset="1" stop-color="var(--blue-light)"/></linearGradient></defs>
    <polygon points="0,0 72,0 72,50 0,90" fill="url(#planCard)"/>
  </svg>
  <div class="brand"><span class="brand-mark"></span>VERANOX</div>
  <div class="person">
    <div class="name">Milo Harwick</div>
    <div class="role">Associate</div>
    <div>milo.harwick@veranox.example</div>
    <div class="gap"></div>
    <div>Veranox Partners Suite 4, The Yard</div>
    <div>Kestrel Park, Ashford, AS12 3QR</div>
    <div>T : 01632 960412</div>
    <div>F : 01632 960587</div>
  </div>
  <div class="note">With Compliments</div>
</section>

<section class="sheet card-back">
  <svg class="plan-area" width="355" height="190" role="img" aria-label="Blue architectural floor plan drawing">
    <defs><linearGradient id="planBack" x1="0" y1="0" x2="1" y2="1"><stop offset="0" stop-color="var(--blue-dark)"/><stop offset="1" stop-color="var(--blue-light)"/></linearGradient></defs>
    <path d="M0,0 H150 C110,60 70,120 40,190 H0 Z" fill="url(#planBack)"/>
  </svg>
  <div class="brand"><span class="brand-mark"></span>VERANOX</div>
</section>

<section class="sheet comp-slip">
  <svg class="plan-area" width="220" height="200" role="img" aria-label="Blue architectural floor plan drawing">
    <defs><linearGradient id="planSlip" x1="0" y1="0" x2="1" y2="1"><stop offset="0" stop-color="var(--blue-dark)"/><stop offset="1" stop-color="var(--blue-light)"/></linearGradient></defs>
    <polygon points="0,0 190,0 190,70 0,175" fill="url(#planSlip)"/>
  </svg>
  <div class="brand"><span class="brand-mark"></span>VERANOX</div>
  <div class="note">With Compliments</div>
  <div class="footer">
    <span>Veranox Partners Suite 4, The Yard</span>
    <span>Kestrel Park, Ashford, AS12 3QR</span>
    <span>Telephone 01632 960412</span>
    <span>Fax 01632 960587</span>
    <span>www.veranox.example</span>
  </div>
</section>

</body>
</html>
```